Create Lanternfield HR Business Cards.

Create Business Cards for Lanternfield HR. 2 sided and Would like the back to have the logo.

Info for Business Card:
Address: 4827 Millbrook Ave Suite 230 Cleveland, Ohio 44987
Office Number: 216-555-0143
Mobile: 216-555-0192

Website: www.lanternfieldhr.example

Target Market(s)

Small to medium size businesses

Industry/Entity Type

Human Resources

Contact Information for Business Card

Company logo and information

Font styles to use
Serif
Sans Serif

Requirements
Must have
• Info for Business Card: Address: 4827 Millbrook Ave Suite 230 Cleveland, Ohio 44987 Office Number: 216-555-0143 Mobile: 216-555-0192 Website: www.lanternfieldhr.example

```html
<!DOCTYPE html>
<html lang="en">
<head>
<meta charset="utf-8">
<title>Lanternfield HR Business Cards</title>
<link href="https://fonts.googleapis.com/css2?family=Montserrat:wght@700&family=Roboto:wght@300;400&display=swap" rel="stylesheet">
<style>
  :root {
    --backdrop: #d2d7d5;
    --card: #f5f5f2;
    --navy: #1c1a45;
    --orange: #e06a12;
    --ink: #3a3a44;
  }
  * { margin: 0; padding: 0; box-sizing: border-box; }
  html, body { width: 1200px; height: 1050px; overflow: hidden; }
  body {
    background: var(--backdrop);
    font-family: "Roboto", sans-serif;
    position: relative;
  }
  .card {
    position: absolute;
    left: 250px;
    width: 700px;
    height: 400px;
    background: var(--card);
    border-radius: 4px;
    box-shadow: 0 6px 18px rgba(0,0,0,0.12);
  }
  .card--front { top: 90px; }
  .card--back { top: 560px; display: flex; align-items: center; justify-content: center; }

  .brand { display: flex; align-items: center; gap: 12px; }
  .brand__dot { width: 26px; height: 26px; border-radius: 50%; background: var(--orange); flex: none; }
  .brand__name {
    font-family: "Montserrat", sans-serif;
    font-weight: 700;
    color: var(--navy);
    letter-spacing: 0.04em;
    text-transform: uppercase;
    line-height: 1.1;
  }
  .card--front .brand { position: absolute; left: 40px; top: 170px; width: 240px; }
  .card--front .brand__name { font-size: 22px; }
  .card--back .brand__dot { width: 40px; height: 40px; }
  .card--back .brand__name { font-size: 40px; }

  .divider { position: absolute; left: 300px; top: 80px; width: 2px; height: 240px; background: var(--navy); }

  .details { position: absolute; left: 330px; top: 82px; right: 24px; }
  .details__name {
    font-family: "Montserrat", sans-serif;
    font-weight: 700;
    font-size: 25px;
    color: var(--navy);
    text-transform: uppercase;
    letter-spacing: 0.02em;
  }
  .details__title { font-weight: 300; font-size: 21px; color: var(--orange); margin-top: 2px; }
  .details__address { font-size: 17px; color: var(--ink); margin-top: 14px; line-height: 1.35; }
  .contact { list-style: none; margin-top: 14px; }
  .contact__item { display: flex; align-items: center; gap: 10px; font-size: 17px; color: var(--ink); line-height: 1.55; }
  .contact__icon { width: 16px; height: 16px; flex: none; }
</style>
</head>
<body>
  <section class="card card--front" aria-label="Business card front">
    <div class="brand">
      <span class="brand__dot"></span>
      <span class="brand__name">Lanternfield HR</span>
    </div>
    <div class="divider"></div>
    <div class="details">
      <p class="details__name">Dorian Vellacott</p>
      <p class="details__title">Managing Director</p>
      <p class="details__address">4827 Millbrook Ave Suite 230<br>Cleveland, Ohio 44987</p>
      <ul class="contact">
        <li class="contact__item">
          <svg class="contact__icon" viewBox="0 0 16 16" aria-hidden="true"><path fill="#e06a12" d="M2 5c0-2 2-3 6-3s6 1 6 3v1h-3V4.5H5V6H2zM4 7h8l2 7H2zm4 1.5a2 2 0 1 0 0 4 2 2 0 0 0 0-4z"/></svg>
          216-555-0143
        </li>
        <li class="contact__item">
          <svg class="contact__icon" viewBox="0 0 16 16" aria-hidden="true"><rect x="4" y="1" width="8" height="14" rx="1.5" fill="none" stroke="#e06a12" stroke-width="1.6"/><circle cx="8" cy="12.5" r="0.9" fill="#e06a12"/></svg>
          216-555-0192
        </li>
        <li class="contact__item">
          <svg class="contact__icon" viewBox="0 0 16 16" aria-hidden="true"><rect x="1" y="3.5" width="14" height="9" fill="#e06a12"/><path d="M1.5 4l6.5 5 6.5-5" fill="none" stroke="#f5f5f2" stroke-width="1.2"/></svg>
          info@lanternfieldhr.example
        </li>
        <li class="contact__item">
          <svg class="contact__icon" viewBox="0 0 16 16" aria-hidden="true"><circle cx="8" cy="8" r="6.5" fill="none" stroke="#e06a12" stroke-width="1.5"/><ellipse cx="8" cy="8" rx="2.6" ry="6.5" fill="none" stroke="#e06a12" stroke-width="1.2"/><path d="M1.5 8h13" stroke="#e06a12" stroke-width="1.2"/></svg>
          www.lanternfieldhr.example
        </li>
      </ul>
    </div>
  </section>

  <section class="card card--back" aria-label="Business card back">
    <div class="brand">
      <span class="brand__dot"></span>
      <span class="brand__name">Lanternfield HR</span>
    </div>
  </section>
</body>
</html>
```